Honey apple cider vinegar label

organic food company need a contemporary honey apple cider vinegar and honey vinegar label, natural GMP logo HACCP LOgo
label detail height :140mm Width:80mm
ingredient: honey, apple cider vinegar and water, free from artificial color & preservative
Shelf Life: 3 years
Net weight 400ml
Storage : store in cool place , do not expose to sunlight
instruction for use: add 20ml to a full glass of water 3, times a days before meal, stop consuming if allergies happen
certification, GMP HACCP, Halal, natural product

Target Market(s)

health conscious group

Requirements
Must have
• modern feel, honey and apple picture

```html
<!DOCTYPE html>
<html lang="en">
<head>
<meta charset="UTF-8">
<title>Honey Apple Cider Vinegar Label</title>
<link href="https://fonts.googleapis.com/css2?family=Playfair+Display:wght@400;700&family=Arimo:wght@400;700&family=Cinzel:wght@400;700&display=swap" rel="stylesheet">
<style>
  :root {
    --honey: #f8d12c;
    --honey-light: #fbe27a;
    --honey-deep: #f0b81e;
    --charcoal: #2e2f30;
    --vinegar-red: #b3121d;
    --leaf-green: #6fb23a;
    --badge-green: #3f9a3a;
    --white: #ffffff;
    --ink: #1c1c1c;
    --apple-red: #c8151f;
  }
  html, body {
    margin: 0;
    padding: 0;
    overflow: hidden;
    background: #ffffff;
  }
  .label {
    position: relative;
    width: 687px;
    height: 1200px;
    overflow: hidden;
    background: var(--honey);
    font-family: "Arimo", sans-serif;
  }
  .honeycomb-field {
    position: absolute;
    inset: 0;
    background: radial-gradient(circle at 50% 40%, var(--honey-light) 0%, var(--honey) 55%, var(--honey-deep) 100%);
  }
  .front-panel {
    position: absolute;
    left: 46px;
    top: 0;
    width: 595px;
    height: 859px;
    background: var(--charcoal);
  }
  .tagline {
    position: absolute;
    top: 30px;
    left: 0;
    width: 100%;
    text-align: center;
    color: var(--leaf-green);
    font-size: 24px;
    margin: 0;
  }
  .brand-seal {
    position: absolute;
    left: 218px;
    top: 62px;
    width: 252px;
    height: 252px;
    border-radius: 50%;
    background: var(--white);
    display: flex;
    flex-direction: column;
    align-items: center;
    justify-content: center;
  }
  .brand-name {
    font-size: 46px;
    font-weight: 700;
    color: var(--charcoal);
    line-height: 1;
    margin-top: 50px;
  }
  .brand-sub {
    font-size: 22px;
    font-weight: 700;
    color: var(--charcoal);
    line-height: 1;
    margin-top: 4px;
  }
  .apple-art {
    position: absolute;
    left: 462px;
    top: 362px;
    width: 200px;
    height: 190px;
    border-radius: 45% 45% 40% 40%;
    background: radial-gradient(circle at 35% 40%, #e5333b 0%, var(--apple-red) 50%, #7e0d12 100%);
  }
  .honey-art {
    position: absolute;
    left: 36px;
    top: 492px;
    width: 170px;
    height: 200px;
    border-radius: 18px;
    background: radial-gradient(circle at 45% 45%, #f7b928 0%, #e08f10 60%, #a9600a 100%);
  }
  .product-title {
    position: absolute;
    left: 0;
    top: 318px;
    width: 100%;
    height: 360px;
    margin: 0;
    font-family: "Playfair Display", serif;
    font-weight: 400;
    color: var(--white);
    line-height: 1;
    z-index: 2;
  }
  .title-honey,
  .title-apple {
    position: absolute;
    display: block;
    font-size: 150px;
    transform: scaleX(0.62);
    transform-origin: left top;
    white-space: nowrap;
  }
  .title-honey { left: 128px; top: 0; }
  .title-apple { left: 256px; top: 168px; }
  .variant-band {
    position: absolute;
    left: 0;
    top: 762px;
    width: 100%;
    height: 62px;
    background: var(--vinegar-red);
    display: flex;
    align-items: center;
    justify-content: center;
  }
  .variant-name {
    margin: 0;
    font-family: "Cinzel", serif;
    font-weight: 400;
    font-size: 42px;
    letter-spacing: 9px;
    color: var(--white);
  }
  .cert-badge {
    position: absolute;
    top: 1040px;
    width: 112px;
    height: 112px;
    border-radius: 50%;
    background: var(--badge-green);
    border: 4px solid var(--white);
    box-sizing: border-box;
  }
  .cert-badge--left { left: 57px; }
  .cert-badge--right { left: 518px; }
  .net-content {
    position: absolute;
    left: 0;
    top: 1046px;
    width: 100%;
    text-align: center;
    color: var(--ink);
    margin: 0;
  }
  .net-label { display: block; font-size: 25px; }
  .net-value { display: block; font-size: 34px; margin-top: 2px; }
</style>
</head>
<body>
  <main class="label">
    <div class="honeycomb-field" role="img" aria-label="Honeycomb pattern in golden yellow tones"></div>

    <section class="front-panel" aria-label="Front panel"></section>

    <p class="tagline">All Natural</p>

    <div class="brand-seal">
      <span class="brand-name">meadowa</span>
      <span class="brand-sub">organic</span>
    </div>

    <div class="apple-art" role="img" aria-label="Red apple with a cut slice"></div>
    <div class="honey-art" role="img" aria-label="Honeycomb pieces with a wooden honey dipper and dripping honey"></div>

    <h1 class="product-title">
      <span class="title-honey">Honey</span>
      <span class="title-apple">Apple</span>
    </h1>

    <div class="variant-band">
      <h2 class="variant-name">CIDER VINEGAR</h2>
    </div>

    <div class="cert-badge cert-badge--left" role="img" aria-label="Food safety certification badge"></div>
    <div class="cert-badge cert-badge--right" role="img" aria-label="Manufacturing quality certification badge"></div>

    <p class="net-content">
      <span class="net-label">Net weight</span>
      <span class="net-value">400ml</span>
    </p>
  </main>
</body>
</html>
```